Case Management business card

Catastrophic Case Management
I'm looking for a design that best fits the words Bellwood and Catastrophic.
We need a business card for a new business based in Michigan Called Bellwood Restorative Care Coordination Group, LLC.
We provide services to clients who have been injured in a car accident and requires assistance of a case manager to facilitate and collaborate care services with or for them to help them on the road from injury to recovery. We would like to use the colors green and orange. The final design should communicate health maintenance and recovery.
We offer an comprehensive head to toe assessment.
We facilitate collaboration with your personalized injury care team members.
We assist with home and attendant care services.
We have a Team of Case managers who's main focus is continuity of care and recovery from motor vehicle injuries.

Industry/Entity Type

Business

Contact Information for Business Card

Bellwood Restorative Care Coordination Group, LLC
Catastrophic and Medical Case Management Services
2873 N. Carlow # 504318
Fenmarsh Vale 48352
Lorna Vance RN, CM
Director of Case Management
lvance@bellwoodrccg.com
Ph: 555-518-4937
Fax: 555-518-4071

```html
<!DOCTYPE html>
<html lang="en">
<head>
<meta charset="utf-8">
<title>Bellwood Restorative Care Coordination Group — Business Card</title>
<link rel="stylesheet" href="https://fonts.googleapis.com/css2?family=Oswald:wght@500;600&family=Open+Sans:wght@400;600&display=swap">
<style>
  :root {
    --orange: #e0952a;
    --green: #6aab2e;
    --paper: #ffffff;
    --backdrop: #ececec;
    --ink-white: #ffffff;
  }
  * { margin: 0; padding: 0; box-sizing: border-box; }
  html, body { width: 1200px; height: 900px; overflow: hidden; }
  body {
    background: var(--backdrop);
    font-family: "Open Sans", Arial, sans-serif;
    position: relative;
  }
  .card {
    position: absolute;
    top: 296px;
    width: 540px;
    height: 309px;
    box-shadow: 0 2px 10px rgba(0,0,0,0.12);
  }
  .card--front { left: 40px; background: var(--paper); }
  .card--back  { left: 620px; background: var(--orange); }

  /* Front */
  .person { position: absolute; left: 38px; top: 40px; }
  .person__name { color: var(--orange); font-weight: 600; font-size: 17px; }
  .person__title { color: var(--green); font-size: 12px; margin-top: 3px; }

  .contact-list { position: absolute; left: 38px; top: 150px; list-style: none; }
  .contact-list li {
    display: flex; align-items: center; gap: 9px;
    color: var(--green); font-size: 11.5px; line-height: 22px;
    white-space: nowrap;
  }
  .contact-list svg { width: 11px; height: 11px; fill: var(--orange); flex: none; }

  .brand { position: absolute; left: 292px; top: 140px; width: 230px; }
  .brand__row { display: flex; align-items: center; gap: 7px; }
  .brand__dot { width: 14px; height: 14px; border-radius: 50%; background: var(--orange); flex: none; }
  .brand__name {
    font-family: "Oswald", "Arial Narrow", sans-serif;
    font-weight: 600; color: var(--green);
    font-size: 14px; line-height: 1.1; text-transform: uppercase; letter-spacing: 0.3px;
  }
  .brand__tagline {
    margin-top: 4px; margin-left: 21px;
    color: var(--green); font-size: 6.5px; text-transform: uppercase; letter-spacing: 0.3px;
    white-space: nowrap;
  }

  /* Back */
  .back-mark {
    position: absolute; left: 0; right: 0; top: 96px;
    text-align: center; color: var(--ink-white);
  }
  .back-mark__name {
    font-family: "Oswald", "Arial Narrow", sans-serif;
    font-weight: 600; text-transform: uppercase;
    font-size: 26px; line-height: 1.08; letter-spacing: 0.4px;
  }
  .back-mark__tagline {
    margin-top: 6px;
    font-family: "Open Sans", Arial, sans-serif; font-weight: 600;
    font-size: 9.5px; text-transform: uppercase; letter-spacing: 1px;
  }
</style>
</head>
<body>

<section class="card card--front">
  <div class="person">
    <p class="person__name">Lorna Vance RN, CM</p>
    <p class="person__title">Director of Case Management</p>
  </div>

  <ul class="contact-list">
    <li>
      <svg viewBox="0 0 24 24"><path d="M6.6 10.8a15.1 15.1 0 0 0 6.6 6.6l2.2-2.2a1 1 0 0 1 1-.25 11.4 11.4 0 0 0 3.6.57 1 1 0 0 1 1 1V20a1 1 0 0 1-1 1A17 17 0 0 1 3 4a1 1 0 0 1 1-1h3.5a1 1 0 0 1 1 1c0 1.25.2 2.45.57 3.57a1 1 0 0 1-.25 1z"/></svg>
      555-518-4937
    </li>
    <li>
      <svg viewBox="0 0 24 24"><path d="M6 2h10l2 2v5H6zM3 10h18a1 1 0 0 1 1 1v7h-4v4H6v-4H2v-7a1 1 0 0 1 1-1zm5 7v3h8v-3z"/></svg>
      555-518-4071
    </li>
    <li>
      <svg viewBox="0 0 24 24"><path d="M2 5h20v14H2zm2 2v.5l8 5 8-5V7z"/></svg>
      lvance@bellwoodrccg.com
    </li>
    <li>
      <svg viewBox="0 0 24 24"><path d="M12 2a7 7 0 0 1 7 7c0 5-7 13-7 13S5 14 5 9a7 7 0 0 1 7-7zm0 4.5A2.5 2.5 0 1 0 12 11.5 2.5 2.5 0 0 0 12 6.5z"/></svg>
      2873 N. Carlow # 504318 Fenmarsh Vale 48352
    </li>
  </ul>

  <div class="brand">
    <div class="brand__row">
      <span class="brand__dot"></span>
      <p class="brand__name">Bellwood Restorative Care<br>Coordination Group, LLC</p>
    </div>
    <p class="brand__tagline">Catastrophic and Medical Case Management Services</p>
  </div>
</section>

<section class="card card--back">
  <div class="back-mark">
    <p class="back-mark__name">Bellwood Restorative Care<br>Coordination Group, LLC</p>
    <p class="back-mark__tagline">Catastrophic and Medical Case Management Services</p>
  </div>
</section>

</body>
</html>
```